Secret agents need a new website

We organize child birthdays with a special agents in london & Bristol.

Current design does not grab people attention, and they leave website too soon.

Colors. Up to 3 main colors, but maybe black + green + white, or blact + red + white, would suit our secret operations website.

Current website:
www.jollyfete.co.uk

Dear designers, thanks very much for working on our design.

Please try to make like a SPECIAL YOUNG AGENT TRAINING WEBSITE, all other
entertainers have childish websites, and we want to differentiate from them.

Not sure if it helps, but I like this design very much:

Guys,

I am looking for spy/secret agent/action themed design. You submitting awesome designs, and if I have another business, I just choose any of them at it would be perfect. But I want spy/secret agent/action themed.

Please feel free to add elements like:

1. Yellow, or RED line CRIME SCENE DO NOT CROSS
2. Some words or phrases can be black background - white text. 
3. Some stamps like this:
http://www.pixelvarn.com/pic-71829455/stock-vector-various-security-rubber-stamps-top-secret-confidential-etc.html?src=pQt8Lm-zRwXeN3a-k57HvB-1-16

4.spy guys http://www.pixelvarn.com/pic-48213907/stock-vector-detective-in-trench-coat-retro-clip-art.html?src=hwTbRsJePo4K2nxtmcVfUQ-1-9

Do not make too much elements, I like simple designs, less details.  

PLEASE NO CHILDS WITH GUNS, and better NO GUNS at all. 

Target Market(s)

Audience: Woman, but should look cool for kids too.
(Please DO NOT make design childish)

Requirements
Must have
• Please take a look at current website
• 1. Texts should be easy to read and not too small.
• 2. White/bright background
• 3. Lead form should stay on page
• 4. Header, and footer should be not too big.
• 5. Infographic is not needed
• Extra elements
• 1. Company blog
• 2. Client zone
• 3. Venue finder
• 4. How to pay deposit
Nice to have
• We accept
• Coinvey
• morwells
• (please browse logos)
• On header would be better to use
• JollyFete.co.uk
• But also add somethere, in association with Tin-kettle.co.uk.
• Please use logo with .co.uk
• In archive you will find without background if needed too.

```html
<!DOCTYPE html>
<html lang="en">
<head>
<meta charset="utf-8">
<title>Tin-kettle.co.uk – Spy Kid Birthday Parties</title>
<link href="https://fonts.googleapis.com/css2?family=Chewy&family=Russo+One&family=Oswald:wght@300;400&family=Baloo+2:wght@600;700&family=Mulish:wght@400&family=Arimo&display=swap" rel="stylesheet">
<style>
  :root {
    --green: #8cc63f;
    --nav-green: #a2e036;
    --red: #e35252;
    --ink: #26242f;
    --nav-bg: #2b2a38;
    --band: #2c2c2c;
    --hill: #e0eecb;
    --paper: #ececec;
    --text: #3b3b3b;
    --grey-text: #707070;
  }
  * { box-sizing: border-box; margin: 0; padding: 0; }
  html, body { width: 1200px; height: 960px; overflow: hidden; }
  body { position: relative; background: var(--paper); font-family: "Mulish", sans-serif; }

  .site-header { position: absolute; left: 0; top: 0; width: 1200px; height: 105px;
    background: linear-gradient(90deg, #fff 0%, #f2f2f2 40%, #dedede 100%); }
  .brand { position: absolute; left: 34px; top: 38px; display: flex; align-items: center; gap: 8px;
    font-family: "Baloo 2", sans-serif; font-weight: 700; font-size: 28px; color: var(--green); }
  .brand-dot { width: 14px; height: 14px; background: var(--ink); }
  .contact-tab { position: absolute; left: 866px; top: 0; width: 340px; height: 32px;
    background: var(--nav-bg); border: 2px solid var(--green); border-top: none; border-right: none;
    border-bottom-left-radius: 16px; font-family: "Baloo 2", sans-serif; font-weight: 700; color: var(--nav-green); }
  .contact-tab .enquiry-link { position: absolute; left: 28px; top: 3px; font-size: 15px; }
  .contact-tab .phone { position: absolute; right: 14px; top: 2px; font-size: 14px; }
  .contact-tab .phone b { font-size: 17px; letter-spacing: 0.5px; margin-left: 4px; }

  .main-nav { position: absolute; left: 0; top: 105px; width: 1200px; height: 31px; background: var(--nav-bg); }
  .main-nav a { position: absolute; top: 4px; font-family: "Oswald", sans-serif; font-weight: 400;
    font-size: 18px; letter-spacing: 1.5px; color: var(--nav-green); text-decoration: none; }
  .main-nav .active::before { content: ""; position: absolute; left: -2px; top: -9px; width: 46px; height: 5px; background: var(--red); }

  .hero { position: absolute; left: 0; top: 136px; width: 1200px; height: 306px; background: #fff; overflow: hidden; }
  .hero-hill { position: absolute; left: 0; top: 0; }
  .hero-title { position: absolute; left: 214px; top: 44px; font-family: "Chewy", cursive;
    font-size: 50px; line-height: 60px; font-weight: 400; color: var(--green); white-space: nowrap; }
  .hero-sub { position: absolute; left: 216px; top: 120px; font-family: "Russo One", sans-serif;
    font-size: 46px; line-height: 52px; font-style: italic; color: var(--ink); letter-spacing: 2px; white-space: nowrap; }
  .hero-lead { position: absolute; left: 213px; top: 188px; width: 320px; font-family: "Oswald", sans-serif;
    font-weight: 300; font-size: 16px; line-height: 21px; color: var(--grey-text); text-transform: uppercase; }
  .hero-glasses { position: absolute; left: 294px; top: 244px; width: 102px; height: 36px; border-radius: 12px;
    background: linear-gradient(#4a4a4a, #1e1e1e); }
  .hero-agent { position: absolute; left: 640px; top: 16px; width: 190px; height: 290px;
    border-radius: 70px 70px 0 0; background: linear-gradient(#d9c2a6 0%, #c9b193 28%, #2f2f36 40%, #222229 100%); }
  .testimonial { position: absolute; left: 852px; top: 26px; width: 135px; height: 150px; }
  .testimonial p { position: absolute; left: 29px; top: 0; width: 110px; font-family: "Baloo 2", sans-serif;
    font-weight: 600; font-size: 14.5px; line-height: 17.4px; color: var(--red); white-space: nowrap; }
  .testimonial .mark { position: absolute; }

  .quote-band { position: absolute; left: 0; top: 442px; width: 1200px; height: 198px; background: var(--band);
    border-top: 3px solid #7bc043; }
  .video-frame { position: absolute; left: 216px; top: 15px; width: 297px; height: 168px;
    background: linear-gradient(#3a3330, #b08f6c 45%, #6e5a48); }
  .video-frame .bar { position: absolute; left: 0; bottom: 0; width: 100%; height: 14px; background: #111; }
  .video-frame .progress { position: absolute; left: 0; bottom: 14px; width: 75px; height: 3px; background: #d22; }

  .quote-form { position: absolute; left: 595px; top: 21px; width: 389px; height: 166px; border-radius: 16px;
    background: linear-gradient(#fff 0%, #f1f1f1 35%, #a9a9a9 100%); }
  .quote-form h2 { position: absolute; left: 0; top: 7px; width: 100%; text-align: center;
    font-family: "Baloo 2", sans-serif; font-weight: 700; font-size: 15px; color: var(--red); }
  .field { position: absolute; width: 140px; height: 23px; background: #fff; border: none;
    font-family: "Arimo", sans-serif; font-size: 10px; color: #333; padding-left: 35px; line-height: 23px; }
  .form-note { position: absolute; left: 16px; top: 150px; font-family: "Arimo", sans-serif; font-size: 10px; color: #fff; }
  .submit { position: absolute; left: 244px; top: 126px; width: 138px; height: 35px; border-radius: 18px;
    background: var(--red); color: #fff; font-family: "Baloo 2", sans-serif; font-weight: 700; font-size: 15px;
    letter-spacing: 1px; text-align: center; line-height: 37px; }

  .intro { position: absolute; left: 216px; top: 655px; width: 366px; font-size: 12.6px; line-height: 15.4px; color: var(--text); }
  .intro p + p { margin-top: 15.4px; }
  .intro p.tight { margin-top: 0; }
  .gallery-photo { position: absolute; }
</style>
</head>
<body>
  <header class="site-header">
    <div class="brand"><span class="brand-dot"></span>Tin-kettle.co.uk</div>
    <div class="contact-tab">
      <span class="enquiry-link">Enquiry</span>
      <span class="phone">Call Us: <b>020 4000 5123</b></span>
    </div>
  </header>

  <nav class="main-nav">
    <a class="active" style="left:316px">HOME</a>
    <a style="left:404px">EQUIPMENT</a>
    <a style="left:536px">INVITATIONS</a>
    <a style="left:678px">PARTY BAGS</a>
    <a style="left:821px">PRICES</a>
  </nav>

  <section class="hero">
    <svg class="hero-hill" width="1200" height="306" viewBox="0 0 1200 306" aria-hidden="true">
      <path d="M0 262 C120 250 220 230 300 190 C380 150 460 120 560 130 C660 140 720 200 800 220 C880 240 940 220 1010 232 C1080 244 1140 262 1200 262 L1200 306 L0 306 Z" fill="var(--hill)"/>
    </svg>
    <h1 class="hero-title">Happy Birthday</h1>
    <div class="hero-sub">SPY KID !!!</div>
    <p class="hero-lead">Capture your kids imagination with a spy birthday party in London, Bristol</p>
    <div class="hero-glasses" role="img" aria-label="Pair of dark spy sunglasses"></div>
    <div class="hero-agent" role="img" aria-label="Photo of a young boy in a suit and sunglasses giving a thumbs up"></div>
    <blockquote class="testimonial">
      <svg class="mark" style="left:2px;top:-2px" width="24" height="16" viewBox="0 0 24 16" aria-hidden="true">
        <path d="M6 0 H12 L6 16 H0 Z M17 0 H23 L17 16 H11 Z" fill="var(--red)"/>
      </svg>
      <p>I wanted a<br>kids birthday<br>party with a<br>difference,<br>and then I<br>found the Top<br>Secret Spy<br>Party</p>
      <svg class="mark" style="left:108px;top:134px" width="24" height="16" viewBox="0 0 24 16" aria-hidden="true">
        <path d="M6 0 H12 L6 16 H0 Z M17 0 H23 L17 16 H11 Z" fill="var(--red)"/>
      </svg>
    </blockquote>
  </section>

  <section class="quote-band">
    <div class="video-frame" role="img" aria-label="Video of children at a spy birthday party using metal detectors">
      <span class="progress"></span><span class="bar"></span>
    </div>
    <form class="quote-form">
      <h2>Request a Quote Now !</h2>
      <div class="field" style="left:24px;top:48px">your name</div>
      <div class="field" style="left:200px;top:48px">your phone</div>
      <div class="field" style="left:24px;top:80px">your email</div>
      <div class="field" style="left:24px;top:112px">your city</div>
      <div class="form-note">We will respond within 24 hours Monday - Friday.</div>
      <div class="submit">ENQUIRY</div>
    </form>
  </section>

  <article class="intro">
    <p>Every parent wants to give their child the best birthday party, but we don’t always have the time to plan and prepare for an extra special birthday party with the wow factor.</p>
    <p>We created this Spy party to be fun from beginning to end. Your child will send their guests colour top secret invitations to a party where they will take part in Secret Agent Training. The children will be so excited that they won’t be able to stop talking about it.</p>
    <p class="tight">At the party all the children will become special agents, trying out spy gear and finding out how to be a good spy in our fun secret agent games. It's a great way to get the children interested in new things, working together in teams and using their imagination. Every child that takes part will receive a ‘Spy School Secret Agent' certificate and a Spy Party Bag to take away and continue the fun with their friends at home and at school.</p>
  </article>

  <div class="gallery-photo" style="left:593px;top:652px;width:98px;height:148px;background:linear-gradient(#8a6a4a,#e8e2d8)" role="img" aria-label="Photo of a boy in a white shirt holding spy gear"></div>
  <div class="gallery-photo" style="left:693px;top:652px;width:109px;height:148px;background:linear-gradient(#9a7a58,#a79ad4)" role="img" aria-label="Photo of a girl in sunglasses and a purple shirt"></div>
  <div class="gallery-photo" style="left:778px;top:764px;width:98px;height:148px;background:linear-gradient(#6d5643,#e6e6ea 60%,#3a2a24)" role="img" aria-label="Photo of a boy working on a spy gadget"></div>
  <div class="gallery-photo" style="left:878px;top:764px;width:99px;height:148px;background:linear-gradient(#c79a76,#e2793c 55%,#b84a2a)" role="img" aria-label="Photo of a smiling boy in an orange shirt with a spy kit"></div>
</body>
</html>
```